website refresh/redesign needed for Printing e commerce website

We'd like a website refresh/redesign done with the specific goal of having the site act as a more effective funnel for leads.<br/><br/>We think that the current design is outdated.<br/><br/>We want our customers and partners to still recognize the website, Is a big chunk of our business is repeat orders. <br/>so it should not be a full redesign. General color scheme and such should remain the same so that it is clear we are the same company. <br/><br/>However, the updated website design should look more polished and convey high-quality products and services that we provide. <br/><br/>Our website is https://shopledgerformsnet.quillpaperdepot.com/ if you want to take a look at our current website design. <br/><br/>we need 3 pages redesigned... <br/><br/>1. homepage:https://shopledgerformsnet.quillpaperdepot.com/<br/><br/>2. Category page: <br/>https://shopledgerformsnet.quillpaperdepot.com/order-computer-checks-c-4.html<br/><br/>3. Product detail page: https://shopledgerformsnet.quillpaperdepot.com/voucher-computer-checks-p-35.html<br/><br/> I can provide many more pictures of our products if needed.<br/><br/><br/>BTW. I have another project here on brief bazaar, you can check the other ones too, so to make it easier to do both when working on this.<br/><br/> Please reach out to me should you have any questions or comments.

```html
<!DOCTYPE html>
<html lang="en">
<head>
<meta charset="utf-8">
<title>LedgerFormsShop — Business Checks</title>
<link rel="stylesheet" href="https://fonts.googleapis.com/css2?family=Roboto:wght@300;400;500;700&display=swap">
<style>
:root{
  --green-dark:#2f5a1c;
  --green-deep:#234a14;
  --green-bright:#8bea6a;
  --slate:#2f4550;
  --slate-field:#253a44;
  --ink:#333;
  --muted:#666;
  --price:#c0282b;
  --line:#cfcfcf;
  --paper:#f4f4f4;
  --tile:#c5e3e3;
  --blue:#3b8fd8;
  --footer:#2b2b2b;
}
*{box-sizing:border-box;margin:0;padding:0}
html,body{width:1200px;height:3338px;overflow:hidden}
body{font-family:'Roboto',sans-serif;color:var(--ink);background:#fff;position:relative}
.abs{position:absolute}
.topbar{left:0;top:0;width:1200px;height:75px;background:var(--green-dark)}
.brand{left:175px;top:22px;display:flex;align-items:center;gap:8px;color:var(--green-bright);font-size:22px;font-weight:500}
.brand .dot{width:14px;height:14px;background:var(--green-bright)}
.search{left:465px;top:22px;width:342px;height:30px;background:#fff;border-radius:2px;font-size:11px;color:#999;padding:8px 10px}
.search svg{position:absolute;right:10px;top:9px}
.account{left:864px;top:30px;color:#fff;font-size:11px;display:flex;gap:22px}
.nav{left:0;top:75px;width:1200px;height:38px;background:#fff;border-bottom:1px solid #ddd}
.nav ul{list-style:none;display:flex;position:absolute;left:172px;top:0;height:38px}
.nav li{font-size:11px;padding:0 16px;line-height:38px;border-right:1px solid #e2e2e2;color:#333}
.nav li.active{background:var(--green-bright);color:var(--green-deep)}
.nav li.reorder{background:var(--green-bright);color:var(--green-deep);font-weight:500;padding:0 22px}
.hero{left:0;top:113px;width:1200px;height:571px;background:linear-gradient(135deg,#d8d8d0 0%,#a9a8a0 35%,#5a4c70 55%,#3b6b26 85%,#2e5a1c 100%)}
.hero-arrow{top:200px;width:26px;height:48px;background:var(--slate);display:flex;align-items:center;justify-content:center}
.hero h1{left:180px;top:458px;font-size:38px;font-weight:400;color:#fff}
.hero .perks{left:182px;top:510px;display:flex;gap:30px;color:#fff;font-size:15px}
.perks span{display:flex;align-items:center;gap:8px}
.perks i{width:18px;height:18px;border-radius:50%;background:var(--green-bright);display:inline-block}
.btn-white{background:#fff;color:var(--green-deep);font-size:10px;font-weight:500;text-align:center}
.hero .order{left:701px;top:503px;width:128px;height:36px;line-height:36px}
.panel{left:749px;top:61px;width:287px;height:341px;background:var(--slate);box-shadow:0 2px 6px rgba(0,0,0,.3);color:#fff;padding:0 22px}
.panel .cart{display:flex;justify-content:space-between;align-items:center;height:34px;font-size:15px;margin:0 -22px;padding:0 22px;background:#243742}
.panel .cart a{color:var(--green-bright);font-size:12px;text-decoration:underline}
.panel .count{text-align:right;font-size:11px;margin-top:6px}
.panel h3{font-size:15px;font-weight:500;margin-top:18px;margin-bottom:10px}
.field{height:36px;background:var(--slate-field);border-radius:4px;font-size:12px;line-height:36px;padding-left:32px;margin-bottom:7px}
.check{height:38px;background:#fff;color:var(--green-deep);border-radius:4px;text-align:center;line-height:38px;font-size:13px;font-weight:500}
.panel hr{border:0;border-top:1px solid #4f6570;margin:16px 0 0}
.select{height:36px;background:var(--slate-field);border-radius:4px;font-size:12px;line-height:36px;padding-left:16px;position:relative}
.select:after{content:"";position:absolute;right:12px;top:16px;border:5px solid transparent;border-top-color:#fff}
.section-title{width:1200px;text-align:center;font-size:26px;font-weight:400;color:#333}
.card{width:198px;height:237px;border:1px solid var(--line);text-align:center}
.card .img{height:147px;background:#e9e9e9;display:flex;align-items:center;justify-content:center}
.card .img div{width:170px;height:76px}
.card h4{font-size:13px;font-weight:500;margin-top:16px}
.card p{font-size:10px;color:var(--muted);margin-top:9px}
.card .price{color:var(--price);font-size:13px;margin-top:10px}
.card .price.sm{font-size:11px}
.see{width:114px;height:31px;border:1px solid #555;font-size:10px;line-height:29px;text-align:center}
.banner{left:172px;top:1201px;width:856px;height:116px;border:1px solid var(--line);background:#fafafa;overflow:hidden}
.banner .photo{position:absolute;left:380px;top:0;width:476px;height:116px;background:linear-gradient(90deg,#6b6a66,#a7a59f);clip-path:polygon(60px 0,100% 0,100% 100%,0 100%)}
.banner .small{position:absolute;left:23px;top:30px;font-size:22px;font-weight:300;color:var(--green-dark)}
.banner .big{position:absolute;left:23px;top:56px;font-size:30px;color:var(--green-dark)}
.banner .cta{position:absolute;left:434px;top:44px;font-size:22px;color:#fff;font-weight:300}
.banner .btn{position:absolute;left:715px;top:44px;width:114px;height:30px;background:var(--green-deep);color:#fff;font-size:10px;line-height:30px;text-align:center}
.who{left:0;top:1379px;width:1200px;height:508px;background:var(--paper)}
.who .photo{position:absolute;left:0;top:0;width:513px;height:508px;background:linear-gradient(120deg,#c9c4b8,#7e8a8f 50%,#d8d3c6)}
.who h2{position:absolute;left:553px;top:62px;font-size:26px;font-weight:400}
.who p{position:absolute;left:557px;top:122px;width:485px;font-size:12.6px;line-height:24px;color:#555;text-align:justify}
.who .read{position:absolute;left:559px;top:390px;width:126px;height:37px;border:1px solid #555;font-size:10px;line-height:35px;text-align:center}
.tile{width:197px}
.tile .sheet-wrap{height:155px;background:var(--tile);position:relative}
.sheet{position:absolute;left:50px;top:10px;width:97px;height:135px;background:#fff;box-shadow:0 0 2px rgba(0,0,0,.15)}
.band{position:absolute;left:0;width:97px;height:45px;background:var(--blue);border-top:1px solid #2a6eaa}
.tile p{text-align:center;font-size:13px;font-weight:500;margin-top:14px;line-height:19px}
.reviews{left:0;top:2294px;width:1200px;height:495px;background:linear-gradient(135deg,#2c5419,#1f3f10)}
.reviews h2{position:absolute;width:1200px;top:60px;text-align:center;color:#fff;font-size:26px;font-weight:400}
.quote{position:absolute;left:172px;top:140px;width:856px;height:283px;background:#dcdcdc;text-align:center;color:#555}
.quote p{width:710px;margin:78px auto 0;font-size:13px;line-height:22px}
.quote .who-name{color:var(--green-dark);font-size:15px;margin-top:14px}
.quote .date{font-size:13px;margin-top:12px}
.rev-arrow{position:absolute;top:272px}
.soft{display:flex;gap:19px;left:197px;top:2926px}
.soft div{width:83px;height:56px;background:#dedede;border:1px solid #bbb;font-size:11px;font-weight:500;color:#444;display:flex;align-items:center;justify-content:center;text-align:center}
.footer{left:0;top:3048px;width:1200px;height:237px;background:var(--footer);color:#fff}
.footer h5{position:absolute;top:52px;font-size:15px;font-weight:500;color:var(--green-bright)}
.footer ul{position:absolute;top:96px;list-style:none;font-size:12px}
.footer li{margin-bottom:11px;padding-left:14px;position:relative}
.footer li:before{content:"";position:absolute;left:0;top:3px;border:4px solid transparent;border-left-color:var(--green-bright)}
.social{position:absolute;left:515px;top:89px;display:flex;gap:6px}
.social i{width:25px;height:25px;background:#555;display:block}
.seal{position:absolute;left:516px;top:127px;width:44px;height:44px;border-radius:50%;background:#7a8a3a}
.news-txt{position:absolute;left:702px;top:87px;width:290px;font-size:11.5px;line-height:16px}
.news-in{position:absolute;left:701px;top:123px;width:301px;height:36px;background:#fff;color:#777;font-size:12px;line-height:36px;padding-left:10px}
.news-btn{position:absolute;left:701px;top:167px;width:301px;height:36px;background:var(--green-bright);color:#1a3a0c;font-size:14px;font-weight:500;line-height:36px;text-align:center}
.bottom{left:0;top:3285px;width:1200px;height:53px;background:#1e1e1e;color:#fff;font-size:12px}
.bottom .copy{position:absolute;left:189px;top:19px}
.pay{position:absolute;left:815px;top:18px;display:flex;gap:4px}
.pay i{display:block;width:22px;height:14px;background:#ddd}
.pay i.wide{width:100px}
</style>
</head>
<body>

<header class="abs topbar">
  <div class="abs brand"><span class="dot"></span>LedgerFormsShop</div>
  <div class="abs search">Search by Software Checks
    <svg width="11" height="11" viewBox="0 0 12 12"><circle cx="5" cy="5" r="4" fill="none" stroke="#666" stroke-width="1.5"/><line x1="8" y1="8" x2="11" y2="11" stroke="#666" stroke-width="1.5"/></svg>
  </div>
  <div class="abs account"><span>&#9679; Log In / Register</span><span>&#128722; $0.00</span></div>
</header>

<nav class="abs nav">
  <ul>
    <li class="active">Home</li><li>Business Checks</li><li>Computer Checks</li><li>TallyBooks Checks</li><li>Accessories</li><li>Help/FAQs</li><li>&#128722; View Your Cart</li><li class="reorder">&#8635; Quick Reorder</li>
  </ul>
</nav>

<section class="abs hero" role="img" aria-label="Businessman in a suit holding an open binder of computer checks">
  <div class="abs hero-arrow" style="left:0"><svg width="8" height="12"><path d="M7 1 2 6l5 5" stroke="#fff" fill="none" stroke-width="1.5"/></svg></div>
  <div class="abs hero-arrow" style="left:1174px"><svg width="8" height="12"><path d="M1 1l5 5-5 5" stroke="#fff" fill="none" stroke-width="1.5"/></svg></div>
  <div class="abs panel">
    <div class="cart"><span>&#9673; View Your Cart</span><a>Checkout</a></div>
    <div class="count">0 Item &nbsp;&nbsp; $0.00</div>
    <h3>Order Status</h3>
    <div class="field">Order Number</div>
    <div class="field">Email Address</div>
    <div class="check">CHECK</div>
    <hr>
    <h3>Quick Finder</h3>
    <div class="select">Checks by software</div>
  </div>
  <h1 class="abs">Computer Checks</h1>
  <div class="abs perks"><span><i></i>100% software Compatible</span><span><i></i>Ships within 24hr</span><span><i></i>Free logo</span></div>
  <div class="abs btn-white order">ORDER NOW</div>
</section>

<h2 class="abs section-title" style="top:756px">Best Sellers</h2>

<div class="abs card" style="left:172px;top:835px"><div class="img"><div style="background:#2b8a8f"></div></div><h4>TallyBooks Checks</h4><p>Voucher Checks - 3 Per Page - wallet</p><div class="price">Starts at $12.99</div></div>
<div class="abs card" style="left:391px;top:835px"><div class="img"><div style="background:#d9443a"></div></div><h4>Cashwise Checks</h4><p>Top Check - 3 on Page - wallet</p><div class="price">Starts at $12.99</div></div>
<div class="abs card" style="left:610px;top:835px"><div class="img"><div style="background:#b9a9c9"></div></div><h4>Deposit Slips</h4><p>Manual &amp; Computer Deposit Slips</p><div class="price">Slips at $12.99</div></div>
<div class="abs card" style="left:829px;top:835px"><div class="img"><div style="background:#c9c08a"></div></div><h4>Check Accessories</h4><p>Self-Inking Stamps - Envelopes</p><div class="price sm">Envelopes at $9.99</div></div>
<div class="abs see" style="left:214px;top:1086px">SEE MORE</div>
<div class="abs see" style="left:433px;top:1086px">SEE MORE</div>
<div class="abs see" style="left:653px;top:1086px">SEE MORE</div>
<div class="abs see" style="left:872px;top:1086px">SEE MORE</div>

<div class="abs banner">
  <div class="photo" role="img" aria-label="Hands writing a check beside a laptop"></div>
  <div class="small">Fast Shipping</div>
  <div class="big">Shipping &amp; Turnaround</div>
  <div class="cta">Order TallyBooks Checks</div>
  <div class="btn">ORDER NOW</div>
</div>

<section class="abs who">
  <div class="photo" role="img" aria-label="Smiling office worker with a coffee cup at a laptop"></div>
  <h2>Who we are</h2>
  <p>Welcome to the online ordering system of LedgerFormsShop.com, online ordering at LedgerFormsShop.com provides the most Comprehensive business check experience and selection available online, including traditional Manual desktop checks used with the 7 ring check binder, and an extensive selection of computer checks. Our computer checks are available in many layout styles and colors, and range from layouts compatible for Cobalt TallyBooks software, Cobalt Cashwise to checks compatible with all software developed by Sable, Sable Core formally Sable Plumgrove, Sable Plus formally Sable Plumgrove, and Sable Builder (formerly Sable Site Manager), Sable Enterprise (formerly Sable Granite 90 and 200) Sable Fund Ledger (formerly Sable Trust Accounting).</p>
  <div class="read">READ MORE</div>
</section>

<h2 class="abs section-title" style="top:1960px">Checks By layout</h2>

<div class="abs tile" style="left:172px;top:2026px"><div class="sheet-wrap"><div class="sheet"><div class="band" style="top:0"></div></div></div><p>Voucher Computer Checks</p></div>
<div class="abs tile" style="left:391px;top:2026px"><div class="sheet-wrap"><div class="sheet"><div class="band" style="top:45px"></div></div></div><p>Computer Middle Laser Checks</p></div>
<div class="abs tile" style="left:610px;top:2026px"><div class="sheet-wrap"><div class="sheet"><div class="band" style="top:90px"></div></div></div><p>Computer Bottom Checks</p></div>
<div class="abs tile" style="left:829px;top:2026px"><div class="sheet-wrap"><div class="sheet"><div class="band" style="top:0"></div><div class="band" style="top:45px"></div><div class="band" style="top:90px"></div></div></div><p>Computer 3 Per Page<br>Laser Checks</p></div>

<section class="abs reviews" role="img" aria-label="Mosaic of customer portraits tinted green">
  <h2>What our customers say</h2>
  <div class="quote">
    <p>I just want to thank you for the most recent checks and deposit slip order from you. It's perfect clean. Great quality paper and the customer service were exceptional, and at last very reasonable pricing and low shipping cost. I'll refer you to all my friends- this is the 4rd check order we've purchased from you and found the shopping and shipping experience to be exceptional! Thanks Happy Customers!</p>
    <div class="who-name">Dennis K Reno, NV</div>
    <div class="date">5Th April, 2019</div>
  </div>
  <svg class="rev-arrow" style="left:137px" width="10" height="14"><path d="M8 1 2 7l6 6" stroke="#8bea6a" stroke-width="2.5" fill="none"/></svg>
  <svg class="rev-arrow" style="left:1054px" width="10" height="14"><path d="M2 1l6 6-6 6" stroke="#8bea6a" stroke-width="2.5" fill="none"/></svg>
</section>

<h2 class="abs section-title" style="top:2854px">Checks By Software</h2>
<div class="abs soft">
  <div>TallyBooks</div><div>Cashwise</div><div>Plumgrove</div><div>Sable</div><div>Northwind Ledger</div><div>TitleWorks</div><div>BookEdge</div><div>TitleWorks</div>
</div>

<footer class="abs footer">
  <h5 style="left:202px">Support</h5>
  <ul style="left:189px"><li>Contact Us</li><li>Shipping &amp; Turnaround</li><li>Help FAQs</li><li>Order Status</li><li>Reorder</li></ul>
  <h5 style="left:377px">Information</h5>
  <ul style="left:363px"><li>About Us</li><li>Privacy &amp; Security</li><li>Refunds &amp; Returns</li><li>Terms &amp; Conditions</li><li>Rush Order</li></ul>
  <h5 style="left:513px">Stay in touch</h5>
  <div class="social"><i></i><i></i><i></i><i></i></div>
  <div class="seal"></div>
  <h5 style="left:703px">Get our Newsletter</h5>
  <div class="news-txt">Subscribe to our newsletter to get updates about our new products</div>
  <div class="news-in">Enter your email address</div>
  <div class="news-btn">SUBSCRIBE</div>
</footer>

<div class="abs bottom">
  <div class="copy">Copyright © 2019 LedgerFormsShop.com. | &nbsp; Sitemap &nbsp; |</div>
  <div class="pay"><i></i><i></i><i></i><i class="wide"></i></div>
</div>

</body>
</html>
```